buisnes card for Tranquil Footpath

I need a new business card with my information
Brunhilde Ostrova
BKTPA,LMVD,RN(Grermany)
Cranio-Sacral Reflexology
Facial Reflexology, Halvorkmethode TM
Nerve point Reflexology
41672 Meadowcroft Lane
Abbotsford,BC
Tranquilfootpath.ca
I would like the design to show that I work mostly with clients that have health problems.(80% are back/spine related problems).
I would like the card to be professional as well as inviting. I like nature aspects as well.
I have two websites that I like so you have an Idea what kind of design speaks to me.
1. www.harmonelle.ca the craft of mending (Chilliwack)
2.www.gentlearrivalcare.ca (Abbotsford)

My treatment room is blue and the outside of our house is dark blue and grey. That are colors that could be incorporated

Target Market(s)

clients that are looking for a more natural approach to their health issues

Industry/Entity Type

Health And Wellness

Contact Information for Business Card

Brunhilde Ostrova
BKTPA,LMVD,RN(Grermany)
Cranio-Sacral Reflexology
Nerve point Reflexology
41672 Meadowcroft Lane
Abbotsford,BC
Tranquilfootpath.ca

Colors
0355a3
0492cd

Requirements
Must have
• name, address, phonenumber
Nice to have
• 1. www.harmonelle.ca the craft of mending (Chilliwack)
• 2.www.gentlearrivalcare.ca (Abbotsford)
• This are designs that I like.

```html
<!DOCTYPE html>
<html lang="en">
<head>
<meta charset="utf-8">
<title>Brunhilde Ostrova – Tranquil Footpath business card</title>
<link rel="stylesheet" href="https://fonts.googleapis.com/css2?family=Open+Sans:ital,wght@0,400;1,400&display=swap">
<style>
  :root {
    --card-bg: #e8eff8;
    --ink-deep: #0355a3;
    --art-main: #6b95d2;
    --art-light: #8fb0e0;
  }
  html, body {
    margin: 0;
    padding: 0;
    width: 1200px;
    height: 786px;
    overflow: hidden;
    background: var(--card-bg);
  }
  .card {
    position: relative;
    width: 1200px;
    height: 786px;
    background: var(--card-bg);
    font-family: "Open Sans", Arial, sans-serif;
    color: var(--ink-deep);
    overflow: hidden;
  }
  .card__art {
    position: absolute;
    inset: 0;
    width: 1200px;
    height: 786px;
  }
  .card__name {
    position: absolute;
    left: 69px;
    top: 126px;
    margin: 0;
    font-size: 73px;
    line-height: 1.36;
    font-style: italic;
    font-weight: 400;
    letter-spacing: -0.5px;
    color: var(--ink-deep);
    white-space: nowrap;
  }
  .card__services {
    position: absolute;
    left: 69px;
    top: 308px;
    margin: 0;
    padding: 0;
    list-style: none;
    font-size: 46px;
    line-height: 54px;
    color: var(--ink-deep);
    white-space: nowrap;
  }
  .card__contact {
    position: absolute;
    left: 69px;
    top: 590px;
    margin: 0;
    font-style: normal;
    font-size: 36px;
    line-height: 44px;
    color: var(--ink-deep);
  }
  .card__contact span { display: block; white-space: nowrap; }
</style>
</head>
<body>
<main class="card">
  <svg class="card__art" viewBox="0 0 1200 786" role="img" aria-label="Illustration of a hand resting gently against a calm, relaxed face">
    <defs>
      <linearGradient id="artTone" x1="0" y1="0" x2="1" y2="1">
        <stop offset="0" stop-color="#6b95d2"/>
        <stop offset="1" stop-color="#8fb0e0"/>
      </linearGradient>
    </defs>
    <path d="M620 0 H790 C840 160 900 300 980 440 C1060 560 1140 640 1200 690 V786 H1150 C1060 720 960 640 880 540 C790 420 700 250 620 0 Z" fill="url(#artTone)"/>
  </svg>

  <h1 class="card__name">Brunhilde Ostrova</h1>

  <ul class="card__services">
    <li>Cranio-Sacral Reflexology</li>
    <li>Facial Reflexology</li>
    <li>Halvorkmethode TM</li>
    <li>Nerve point Reflexology</li>
  </ul>

  <address class="card__contact">
    <span>Tlf. 604 555 0147</span>
    <span>www.tranquilfootpath.ca</span>
    <span>41672 Meadowcroft Lane. Abbotsford,BC</span>
  </address>
</main>
</body>
</html>
```